Zelmor Africa - Website Design Brief

Web Design Brief

ZELMOR AFRICA
WEBSITE DESIGN BRIEF

INTRODUCTION
ABOUT ZELMOR
• ZELMOR is a premier consulting firm that specialises in aiding global corporations and emerging businesses to enter and scale within Africa's dynamic markets. Through swift, actionable insights and innovative strategies, ZELMOR empowers clients to capitalise on Africa's untapped potential, thereby catering specifically to forward-thinking entities poised for exponential growth.

TASK DESCRIPTION
• Develop a 5-page website for ZELMOR.
• The primary goal is to present a clear and concise picture of our consulting firm, its Africa-centric experience, and its offerings to multinational clients looking for a professional partner to penetrate African markets or reclaim lost market share.

WEBSITE FRAMEWORK
Page Architecture:
• Home
o A powerful landing page that instantly communicates who ZELMOR is and what solutions it provides. Incorporate impactful visuals and calls-to-action.
• About
o A compelling narrative that illustrates ZELMOR's unique approach to consulting, dedication to Africa, and experience assisting multinational firms.
• Services
o A showcase of ZELMOR's successful projects and client testimonials. This page should build trust and credibility, demonstrating ZELMOR's ability to deliver exceptional results.
• Team
o Introduce up to 8 key team members, with each profile featuring a professional photo, name, title, and a brief bio showcasing the individual's skills, experiences, and contributions to ZELMOR's mission.
• Contact
o Clear and easy ways for visitors to contact ZELMOR for more information or to initiate a partnership.
• Footer
o Links to ZELMOR's social media profiles on Instagram and LinkedIn, along with a privacy policy.
o Social links
o Instagram: https://www.instagram.com/zelmorafrica/
o LinkedIn: https://www.linkedin.com/company/zelmorafrica/
o Privacy Policy
o Insert placeholder "lorem ipsum" text.
o Text will be provided with the revision round or ZELMOR will update text on site handover.

DESIGN INSPIRATION
• The website's design should evoke professionalism and elegance, with simple and clean lines inspired by site pages like:
o https://quendaro.example/
o https://quendaro.example/services/
o One aspect we particularly appreciate is how visitors can easily navigate by scrolling down to find what they're looking for and see everything they need to in an intuitive way on the home page
o What we don’t like about this site is how they navigate from the home page to other random pages – we like about to take you to the about page, and so on.

Branding Guidelines:
• See logo on Pixel Bazaar: Design #: 58170926
• We like the idea of the logo being black or white and have uploaded these options as well.
• Monochrome themes, with spots or splash of colour to highlight something is a style we appreciate.

Website Objectives and Goals:
• Our website's primary goal is to create a strong online presence, acting as a hub for potential clients to discover our credibility, reliability, and our ability to deliver exceptional results. It's essential that our website portrays professionalism, instils trustworthiness, and showcases our sincere dedication to Africa.

Target audience:
• ZELMOR's audience consists of businesses in mobile money, gaming, FMCG, beverage, and alcohol sectors, primarily Business Development Managers or Operations Managers who are seeking insight into their respective marketplaces.

Company Overview:
• ZELMOR stands out from the crowd as a consulting firm with a difference. Our dynamic team is fully dedicated to one mission: brand development within Africa.
• Unlike other companies that focus solely on online connectivity, we recognize the tremendous value in embracing the vibrant street culture that makes Africa so unique. Community engagement, empowerment, and expansion are at the forefront of everything we do.
• we recognize that unlocking business growth starts with a deep understanding of consumer behavior. It is this understanding that bridges the gap between companies and the communities that drive the cash economy. Our purpose is to reconnect businesses with the vibrant pulse of these essential local markets, injecting fresh vitality into their brands and propelling them towards resounding success in Africa.

Development to include:
• Basic SEO Setup:
o The website should be optimized for search engines, incorporating keywords, meta tags, and alt tags for images.
• Google Analytics Setup.
o To track website traffic and user behaviour for ongoing optimization.
• Google Crawling Setup
o The website needs to be easily indexed by Google, allowing it to appear in search results, and updated information effectively crawled by Google SEO and AHREFS scores.

PAGE CONTENT:
Home Page
• Background
o Option #1
o 4K video on home page, running on loop
o Bold Statement Text over Video
o Option #2
o Still Image
o Animated text making bold statement (e.g. our motto)

• Sections
o Contrast colour blocks or a way of making it clear that the next topic is a new topic.
o 5 sections
1. Home Main - Video + bold statement text
2. About - A paragraph and visual about us (lorem ipsum) that has a click through to our About Page (ignore how quendaro.example navigate, we think this is too complicated for our needs)
3. Services – communicated in some simple and powerful ways (we leave this open to you) – but keeping in mind it needs to be concise and professional.
4. Other - Something about our process that makes us unique (lorem ipsum text) and a placeholder image/animation.
5. Contact – a call-to-action button that takes you to our contact, but showcases a mobile number and email address.
6. Footer – as described in the previous section – placeholder for Instagram and LinkedIn only.

About Page
• Don’t reference quendaro.example for this page.
• Main Section
o Bold statements and images
• History Section
o A story about us and our past
• Final Section
o Some of our comments and final thoughts

Services Page
• How https://quendaro.example/services/ is laid out is great – we prefer a light theme.
• 6 - 8 x icons with headings and a brief description text box, and a read more drop down – all as placeholders to be edited later.
• For ease of direction for this page, look to the link shared above.

Team
• Add Placeholders for up to 8 team members (we only have 4 now):
o Image placeholder
o Name placeholder
o Title placeholder
o Short Bio (lorem ipsum)

Contact
• Clear and easy ways for visitors to contact ZELMOR for more information or to initiate a partnership.

• Insert placeholder "lorem ipsum" text, we will provide the text with our revision round.
o Ideally an easy form process that gives the user some options or dropdowns to complete before submission – up to 3 would be sufficient.
o Require their name and contact details.

NOTE: Images to follow:

Target Market(s)

ZELMOR's audience consists of businesses in mobile money, gaming, FMCG, beverage, and alcohol sectors, primarily Business Development Managers or Operations Managers who are seeking insight into their respective marketplaces.

Industry/Entity Type

ZELMOR is a premier consulting firm that specialises in aiding global corporations and emerging businesses to enter and scale within Africa's dynamic markets

Coding

Coded - Design and coding required

Number of Pages Required

5+ page

Font styles to use
Sans Serif
Other font styles liked:
• Poppins Font Family

Colors

Designer to choose colors to be used in the design.

Requirements
Must have
• The primary goal is to present a clear and concise picture of our consulting firm, and it's specialisation in Africa - smooth and crisp UI with animations or transitions that imply we know our way around tecchnology is always helpful - but a Clean and responsive UI is most important.
Nice to have
• Reactive and animated transitions through sections or pages - not overdone - adds a professional feel to the site
Should not have
• We don't want too many colours, and we don't want it too dark - we want a monochrome theme, with accents of colour when relevant

```html
<!DOCTYPE html>
<html lang="en">
<head>
<meta charset="utf-8">
<title>ZELMOR – Home</title>
<link href="https://fonts.googleapis.com/css2?family=Montserrat:wght@600;700&family=Inter:ital,wght@0,400;0,500;0,600;0,700;1,400&display=swap" rel="stylesheet">
<style>
:root{
  --ink:#232323;
  --ink-2:#2e2e2e;
  --blue:#0a68b8;
  --blue-deep:#0b5fa8;
  --paper:#f4f8fc;
  --white:#ffffff;
  --text:#333a44;
}
*{box-sizing:border-box;margin:0;padding:0}
html,body{width:1200px;height:3630px;overflow:hidden}
body{position:relative;font-family:"Inter",sans-serif;color:var(--text);background:var(--white)}
.abs{position:absolute}
h1,h2,h3,.brand{font-family:"Montserrat",sans-serif}

/* top bar */
.topbar{left:0;top:0;width:1200px;height:46px;background:var(--ink);color:var(--white);font-size:11px}
.topbar .note{left:0;width:1200px;top:16px;text-align:center}
.dot{width:20px;height:20px;border-radius:50%;background:var(--blue);display:flex;align-items:center;justify-content:center}

/* hero */
.hero{left:0;top:46px;width:1200px;height:704px;
  background:
    radial-gradient(ellipse 420px 300px at 15% 20%,rgba(120,170,220,.35),transparent 70%),
    radial-gradient(ellipse 500px 320px at 85% 75%,rgba(60,140,210,.45),transparent 70%),
    radial-gradient(ellipse 380px 260px at 70% 15%,rgba(20,80,150,.35),transparent 70%),
    linear-gradient(160deg,#2a78c8 0%,#1d64b2 55%,#2b7bcc 100%)}
.brand{color:var(--white);font-weight:600;display:flex;align-items:center;gap:8px}
.brand .mark{border:4px solid var(--white)}
.nav{top:50px;color:var(--white);font-size:11px;font-weight:600}
.nav.active{border-bottom:2px solid var(--white);padding-bottom:4px}
.btn-outline{left:930px;top:36px;width:143px;height:40px;border:1.5px solid var(--white);color:var(--white);font-size:11px;font-weight:600;display:flex;align-items:center;justify-content:center}
.hero h1{left:0;top:318px;width:1200px;text-align:center;color:var(--white);font-size:50px;line-height:52px;font-weight:700}
.hero .lead{left:270px;top:502px;width:660px;text-align:center;color:var(--white);font-size:13px;line-height:19px}
.btn-dark{left:513px;top:576px;width:174px;height:40px;background:var(--ink);color:var(--white);font-size:12px;font-weight:600;display:flex;align-items:center;justify-content:center}

/* about */
.about{left:0;top:750px;width:1200px;height:492px;background:var(--ink)}
.about .block{left:0;top:22px;width:353px;height:446px;background:var(--white)}
.about .block .frame{position:absolute;left:0;top:55px;width:297px;height:334px;background:var(--ink);display:flex;align-items:center;justify-content:center}
.about .block .name{font-family:"Montserrat",sans-serif;font-weight:700;font-size:46px;color:var(--white);letter-spacing:1px}
.about h2{left:432px;top:108px;font-size:52px;color:var(--white);font-weight:700}
.about p{left:432px;top:188px;width:580px;font-size:13px;line-height:21.5px;color:#e8e8e8}
.btn-blue{left:432px;top:330px;width:171px;height:42px;background:var(--blue);color:var(--white);font-size:12px;font-weight:600;display:flex;align-items:center;justify-content:center}

/* services */
.services{left:0;top:1242px;width:1200px;height:1033px;background:var(--paper)}
.services h2{left:125px;top:92px;font-size:52px;color:var(--ink);font-weight:700}
.services .intro{left:125px;top:172px;width:460px;font-size:13px;line-height:21.5px}
.photo-market{left:672px;top:-49px;width:528px;height:549px;
  background:
    radial-gradient(ellipse 220px 160px at 20% 8%,rgba(190,60,50,.75),transparent 70%),
    radial-gradient(ellipse 160px 200px at 45% 35%,rgba(60,150,80,.7),transparent 70%),
    radial-gradient(ellipse 200px 260px at 25% 75%,rgba(200,205,215,.85),transparent 70%),
    radial-gradient(ellipse 220px 320px at 80% 65%,rgba(40,40,45,.9),transparent 70%),
    linear-gradient(135deg,#8a7a68,#6f7a66 45%,#4a4d52)}
.photo-kiosk{left:123px;top:276px;width:307px;height:320px;
  background:
    radial-gradient(ellipse 120px 200px at 50% 45%,rgba(120,100,80,.8),transparent 70%),
    radial-gradient(ellipse 180px 120px at 50% 95%,rgba(150,120,95,.8),transparent 70%),
    linear-gradient(90deg,#3f9a4a,#5aa85a 30%,#5a8f52 70%,#3f9a4a)}
.photo-riders{left:447px;top:276px;width:208px;height:320px;
  background:
    radial-gradient(ellipse 120px 100px at 50% 45%,rgba(60,70,110,.7),transparent 70%),
    linear-gradient(180deg,#c9d3dc 0%,#a89580 35%,#7f6a55 70%,#5a4d40)}
.photo-talk{left:123px;top:613px;width:532px;height:320px;
  background:
    radial-gradient(ellipse 120px 200px at 8% 40%,rgba(200,80,110,.8),transparent 70%),
    radial-gradient(ellipse 140px 120px at 40% 25%,rgba(50,90,170,.8),transparent 70%),
    radial-gradient(ellipse 120px 200px at 72% 50%,rgba(35,45,75,.85),transparent 70%),
    linear-gradient(120deg,#9a8470,#8c7a66 60%,#6e6258)}
.quote-mark{left:715px;top:591px}
.quote{left:715px;top:667px;width:360px;font-size:13px;line-height:21.5px;font-style:italic}
.quote-by{left:715px;top:826px;font-size:15px;font-weight:700;color:var(--blue)}

/* team */
.team{left:0;top:2275px;width:1200px;height:837px;background:var(--blue);color:var(--white);overflow:hidden}
.team .ghost{left:190px;top:20px;width:720px;height:770px;border:100px solid rgba(255,255,255,.035)}
.team h2{left:0;top:92px;width:1200px;text-align:center;font-size:52px;font-weight:700}
.team .intro{left:290px;top:168px;width:620px;text-align:center;font-size:13px;line-height:21.5px}
.card{top:262px;width:225px;height:236px;border:1.5px solid var(--white);background:var(--blue-deep);overflow:hidden}
.card.on{background:var(--white)}
.card .portrait{position:absolute;left:0;top:0;width:100%;height:100%;
  background:radial-gradient(ellipse 95px 70px at 50% 100%,rgba(25,30,40,.7),transparent 80%)}
.card.on .portrait{background:radial-gradient(ellipse 95px 70px at 50% 100%,rgba(80,95,120,.55),transparent 80%)}
.card.light .portrait{background:radial-gradient(ellipse 95px 70px at 50% 100%,rgba(170,205,235,.7),transparent 80%)}
.member{top:532px;width:225px;text-align:center;font-size:20px;font-weight:500}
.bio{left:380px;top:584px;width:200px;text-align:center;font-size:12.5px;line-height:21.5px}
.bio-link{left:380px;top:726px;width:200px;text-align:center;font-size:12px;font-weight:700}
.arrow{top:357px;width:44px;height:44px;border-radius:50%;border:1.5px solid var(--white);display:flex;align-items:center;justify-content:center}

/* footer */
.footer{left:0;top:3112px;width:1200px;height:518px;background:var(--ink);color:var(--white)}
.footer .about-text{left:125px;top:215px;width:345px;font-size:13px;line-height:25px;color:#e0e0e0}
.social{top:338px;width:30px;height:30px;border-radius:50%;background:var(--blue)}
.copy{left:125px;top:398px;font-size:12.5px;color:#e0e0e0}
.contact-box{left:690px;top:68px;width:385px;height:387px;background:var(--ink-2)}
.contact-box h3{position:absolute;left:68px;top:70px;font-size:27px;font-weight:700;letter-spacing:.5px}
.item{position:absolute;left:68px;display:flex;align-items:flex-start;gap:18px;font-size:12.5px;line-height:21px}
.item .dot{width:32px;height:32px;flex:none}
</style>
</head>
<body>

<header class="topbar abs">
  <div class="abs dot" style="left:125px;top:13px"><svg width="10" height="10" viewBox="0 0 24 24"><path fill="#fff" d="M6.6 10.8a15 15 0 006.6 6.6l2.2-2.2a1 1 0 011-.25 11 11 0 003.6.6 1 1 0 011 1V20a1 1 0 01-1 1A17 17 0 013 4a1 1 0 011-1h3.5a1 1 0 011 1 11 11 0 00.6 3.6 1 1 0 01-.25 1z"/></svg></div>
  <div class="abs dot" style="left:162px;top:13px"><svg width="10" height="10" viewBox="0 0 24 24"><rect x="2" y="5" width="20" height="14" fill="#fff"/><path d="M2 5l10 8 10-8" fill="none" stroke="#0a68b8" stroke-width="2"/></svg></div>
  <p class="abs note">Lorem Ipsum is simply dummy text</p>
  <div class="abs dot" style="left:1016px;top:13px"></div>
  <div class="abs dot" style="left:1052px;top:13px"></div>
</header>

<section class="hero abs" role="img" aria-label="Aerial photo of a busy open-air market with colourful umbrellas, tinted blue">
  <div class="abs brand" style="left:125px;top:40px;font-size:30px"><span class="mark" style="width:30px;height:30px"></span>ZELMOR</div>
  <span class="abs nav active" style="left:463px">Home</span>
  <span class="abs nav" style="left:540px">About</span>
  <span class="abs nav" style="left:615px">Services</span>
  <span class="abs nav" style="left:705px">Team</span>
  <a class="abs btn-outline">Contact Us</a>
  <h1 class="abs">ZELMOR Empowers Clients To<br>Capitalize On Africa's Untapped<br>Potential</h1>
  <p class="abs lead">Lorem Ipsum is simply dummy text of the printing and typesetting industry. Lorem Ipsum has been the industry's standard dummy text ever since the 1500s,</p>
  <a class="abs btn-dark">Get Started</a>
</section>

<section class="about abs">
  <div class="abs block">
    <div class="frame"><span class="name">ZELMOR</span></div>
  </div>
  <h2 class="abs">About ZELMOR</h2>
  <p class="abs">ZELMOR is a premier consulting firm that specialises in aiding global corporations and emerging businesses to enter and scale within Africa's dynamic markets. Through swift, actionable insights and innovative strategies, ZELMOR empowers clients to capitalise on Africa's untapped potential, thereby catering specifically to forward-thinking entities poised for exponential growth.</p>
  <a class="abs btn-blue">Read More</a>
</section>

<section class="services abs">
  <h2 class="abs">ZELMOR Services</h2>
  <p class="abs intro">Lorem Ipsum is simply dummy text of the printing and typesetting industry. Lorem Ipsum has been the industry's standard dummy text ever since the 1500s,</p>
  <div class="abs photo-market" role="img" aria-label="Consultant showing a phone to market vendors under a red awning"></div>
  <div class="abs photo-kiosk" role="img" aria-label="People queuing at a green mobile money kiosk"></div>
  <div class="abs photo-riders" role="img" aria-label="Motorbike riders gathered at a market"></div>
  <div class="abs photo-talk" role="img" aria-label="Consultant talking with motorbike taxi riders"></div>
  <svg class="abs quote-mark" width="62" height="42" viewBox="0 0 62 42" aria-hidden="true"><path fill="#0a68b8" d="M0 0h26v22L14 42H4l8-18H0z M36 0h26v22L50 42H40l8-18H36z"/></svg>
  <p class="abs quote">Lorem Ipsum is simply dummy text of the printing and typesetting industry. Lorem Ipsum has been the industry's standard dummy text ever since the 1500s, when an unknown printer took a galley of type and scrambled it to make a type specimen book. It has survived not only five centuries,</p>
  <p class="abs quote-by">Lorem Ipsum</p>
</section>

<section class="team abs">
  <div class="abs ghost"></div>
  <h2 class="abs">Team</h2>
  <p class="abs intro">Lorem Ipsum is simply dummy text of the printing and typesetting industry. Lorem Ipsum has been the industry's standard dummy text ever since the 1500s,</p>
  <div class="abs arrow" style="left:58px"><svg width="14" height="14" viewBox="0 0 14 14"><path d="M9 2L4 7l5 5" fill="none" stroke="#fff" stroke-width="2.4"/></svg></div>
  <div class="abs arrow" style="left:1095px"><svg width="14" height="14" viewBox="0 0 14 14"><path d="M5 2l5 5-5 5" fill="none" stroke="#fff" stroke-width="2.4"/></svg></div>
  <div class="abs card" style="left:125px"><div class="portrait" role="img" aria-label="Team member portrait"></div></div>
  <div class="abs card on" style="left:367px"><div class="portrait" role="img" aria-label="Team member portrait"></div></div>
  <div class="abs card" style="left:608px"><div class="portrait" role="img" aria-label="Team member portrait"></div></div>
  <div class="abs card light" style="left:850px"><div class="portrait" role="img" aria-label="Team member portrait"></div></div>
  <p class="abs member" style="left:125px">Lorem Ipsum</p>
  <p class="abs member" style="left:367px">Lorem Ipsum</p>
  <p class="abs member" style="left:608px">Lorem Ipsum</p>
  <p class="abs member" style="left:850px">Lorem Ipsum</p>
  <p class="abs bio">Lorem Ipsum is simply dummy text of the printing and typesetting industry. Lorem Ipsum has been the industry's standard dummy text ever since the 1500s,</p>
  <p class="abs bio-link">Lorem Ipsum</p>
</section>

<footer class="footer abs">
  <div class="abs brand" style="left:125px;top:100px;font-size:60px;gap:14px"><span class="mark" style="width:66px;height:66px;border-width:6px"></span>ZELMOR</div>
  <p class="abs about-text">Lorem Ipsum is simply dummy text of the printing and typesetting industry. Lorem Ipsum has been the industry's standard dummy text ever since the 1500s,</p>
  <a class="abs social" style="left:125px" aria-label="Instagram"></a>
  <a class="abs social" style="left:175px" aria-label="LinkedIn"></a>
  <p class="abs copy">Copyright@2023-ZELMOR-Privacy Policy</p>
  <div class="abs contact-box">
    <h3>CONTACT</h3>
    <div class="item" style="top:140px"><span class="dot"><svg width="13" height="13" viewBox="0 0 24 24"><path fill="#fff" d="M6.6 10.8a15 15 0 006.6 6.6l2.2-2.2a1 1 0 011-.25 11 11 0 003.6.6 1 1 0 011 1V20a1 1 0 01-1 1A17 17 0 013 4a1 1 0 011-1h3.5a1 1 0 011 1 11 11 0 00.6 3.6 1 1 0 01-.25 1z"/></svg></span><span style="padding-top:5px">800.555.0148</span></div>
    <div class="item" style="top:214px"><span class="dot"><svg width="13" height="13" viewBox="0 0 24 24"><rect x="2" y="5" width="20" height="14" fill="#fff"/><path d="M2 5l10 8 10-8" fill="none" stroke="#0a68b8" stroke-width="2"/></svg></span><span style="padding-top:5px">hello@zelmorafrica.example</span></div>
    <div class="item" style="top:288px"><span class="dot"><svg width="13" height="13" viewBox="0 0 24 24"><path fill="#fff" d="M12 2a7 7 0 017 7c0 5-7 13-7 13S5 14 5 9a7 7 0 017-7z"/><circle cx="12" cy="9" r="2.5" fill="#0a68b8"/></svg></span><span>Lorem Ipsum is simply dummy<br>text of the printing</span></div>
  </div>
</footer>

</body>
</html>
```